CI/CD

I would need Word, PPT, and Excel templates aligned with my website. www.valmorin-consult.ch. I would also need the email footer. Design should look like Brelvox.com

```html
<!DOCTYPE html>
<html lang="de">
<head>
<meta charset="utf-8">
<title>Valmorin Consult – Vorlagen</title>
<link href="https://fonts.googleapis.com/css2?family=Lato:wght@400;700&display=swap" rel="stylesheet">
<style>
  :root{
    --bg:#d8d8d8;
    --navy:#001c3a;
    --navy-mid:#17436e;
    --navy-deep:#0c2a50;
    --orange:#e2602f;
    --white:#ffffff;
    --ink:#111111;
    --shadow:2px 3px 6px rgba(0,0,0,.35);
  }
  *{margin:0;padding:0;box-sizing:border-box}
  html,body{width:1200px;height:960px;overflow:hidden}
  body{background:var(--bg);font-family:"Lato",sans-serif;position:relative}

  .sheet{position:absolute;box-shadow:var(--shadow);overflow:hidden}

  /* Title slide */
  .slide-title{left:58px;top:79px;width:635px;height:355px;background:var(--navy)}
  .slide-title .band{position:absolute;left:207px;top:142px;right:0;height:48px;background:var(--orange)}
  .slide-title .band h1{color:var(--white);font-weight:700;font-size:41px;line-height:48px;padding-left:10px;letter-spacing:-.3px}

  /* Content slide */
  .slide-content{left:58px;top:489px;width:635px;height:357px;background:var(--white)}
  .slide-content .accent-panel{position:absolute;left:414px;top:0;right:0;bottom:0;background:var(--orange)}
  .slide-content .waves,.letterhead .waves{position:absolute;left:0;top:0;width:100%;height:100%}
  .brand{position:absolute;display:flex;align-items:center;gap:4px}
  .brand .dot{border:1.2px solid var(--navy);border-radius:50%}
  .brand .name{color:var(--navy);font-weight:700;white-space:nowrap}
  .slide-content .brand{left:15px;top:24px}
  .slide-content .brand .dot{width:20px;height:20px}
  .slide-content .brand .name{font-size:9px}
  .slide-content .headline{position:absolute;left:88px;top:42px;color:var(--orange);font-weight:700;font-size:20.5px;line-height:24.3px;letter-spacing:-.2px}
  .slide-content .intro{position:absolute;left:88px;top:129px;width:244px;font-size:6.7px;line-height:11.6px;color:var(--ink);text-align:justify}
  .photo-frame{position:absolute;left:360px;top:35px;width:212px;height:161px;background:var(--white)}
  .photo-frame .photo{position:absolute;left:7px;top:8px;width:196px;height:146px;background:linear-gradient(135deg,#8a5a3a 0%,#b9b9b9 45%,#d9dadb 60%,#7a4d33 100%)}
  .page-num{position:absolute;left:23px;top:549px;width:0}
  .slide-content .page-num{left:23px;top:549px}
  .page-badge{position:absolute;left:23px;top:548px;width:13px;height:13px}
  .slide-content .page-badge{left:23px;top:337px;width:13px;height:13px;border-radius:50%;background:var(--orange);color:var(--white);font-size:8px;font-weight:700;line-height:13px;text-align:center}

  /* Letterhead */
  .letterhead{left:748px;top:199px;width:410px;height:557px;background:var(--white)}
  .letterhead .brand{left:15px;top:16px}
  .letterhead .brand .dot{width:17px;height:17px}
  .letterhead .brand .name{font-size:7px}
  .contact{position:absolute;right:59px;top:25px;text-align:right;font-size:5.4px;line-height:7.2px;color:var(--ink)}
  .contact p+p{margin-top:9.6px}
  .contact-rule{position:absolute;left:355px;top:23px;width:1px;height:77px;background:var(--navy-mid)}
  .contact-icons{position:absolute;left:361px;top:26px;width:14px;height:72px}
</style>
</head>
<body>

<section class="sheet slide-title" aria-label="Titelfolie">
  <div class="band"><h1>Welcome</h1></div>
</section>

<section class="sheet slide-content" aria-label="Inhaltsfolie">
  <div class="accent-panel"></div>
  <svg class="waves" viewBox="0 0 1058 596" preserveAspectRatio="none" aria-hidden="true">
    <path d="M0 0 H691 V596 H0 Z" fill="none"/>
    <path d="M0 425 C120 500 300 540 500 545 C700 548 900 480 1058 335 V596 H0 Z" fill="#ffffff"/>
    <path d="M0 425 C120 500 300 540 520 545 C640 546 740 530 790 520 V596 H0 Z" fill="var(--white)"/>
    <path d="M0 425 C130 520 330 548 600 545 C760 538 900 470 1058 335 V596 H0 Z" fill="var(--navy-mid)"/>
    <path d="M0 520 C180 585 420 595 700 596 H0 Z" fill="var(--navy-deep)" opacity=".6"/>
    <path d="M660 596 C760 520 860 460 1058 460 V596 Z" fill="var(--navy-deep)" role="img" aria-label="Architekturfoto mit vertikalen Lamellen in Dunkelblau"/>
    <path d="M0 425 C160 510 380 540 610 540 C760 538 900 480 1058 335" fill="none" stroke="#ffffff" stroke-width="0"/>
  </svg>
  <div class="brand"><span class="dot"></span><span class="name">Valmorin Consult</span></div>
  <h2 class="headline">Für Schweizer KMU.<br>Klarheit, Vertrauen<br>und Zukunft.</h2>
  <p class="intro">Mein Fokus liegt auf Strategie, Innovation und dem bewussten Einsatz von Künstlicher Intelligenz - immer mit Qualität, Klarheit und Verbindlichkeit. Unternehmertum bedeutet für mich Verantwortung für Menschen, Entscheidungen und Zukunft. Seit über 25 Jahren begleite ich Führungskräfte und Teams, damit Wissen Wirkung entfaltet und Orientierung entsteht</p>
  <div class="photo-frame">
    <div class="photo" role="img" aria-label="Foto: Team an einem Besprechungstisch mit Unterlagen und Laptops, von oben"></div>
  </div>
  <div class="page-badge">1</div>
</section>

<section class="sheet letterhead" aria-label="Briefpapier">
  <svg class="waves" viewBox="0 0 683 929" preserveAspectRatio="none" aria-hidden="true">
    <path d="M0 820 C120 880 300 900 520 890 C600 885 650 820 683 765 V929 H0 Z" fill="var(--navy-mid)"/>
    <path d="M0 870 C150 910 320 925 460 929 H0 Z" fill="var(--navy-deep)" opacity=".6"/>
    <path d="M430 929 C500 860 560 830 683 835 V929 Z" fill="var(--navy-deep)" role="img" aria-label="Architekturfoto mit vertikalen Lamellen in Dunkelblau"/>
  </svg>
  <div class="brand"><span class="dot"></span><span class="name">Valmorin Consult</span></div>
  <div class="contact">
    <p>Valmorin Consult<br>Marco Valmorin<br>Lindenhof-Strasse 12</p>
    <p>CH - 8050 Zürich<br>CHE-318.502.771</p>
    <p>Tel.: +41 44 555 01 23<br>info@valmorin-consult.ch</p>
  </div>
  <div class="contact-rule"></div>
  <svg class="contact-icons" viewBox="0 0 14 72" aria-hidden="true">
    <path d="M7 2 a4 4 0 0 1 4 4 c0 3 -4 8 -4 8 s-4 -5 -4 -8 a4 4 0 0 1 4 -4 z" fill="var(--navy-mid)"/>
    <circle cx="7" cy="6" r="1.5" fill="#fff"/>
    <circle cx="6" cy="32" r="2" fill="var(--navy-mid)"/>
    <circle cx="6" cy="40" r="2" fill="var(--navy-mid)"/>
    <path d="M2 57 v9 h2" fill="none" stroke="var(--navy-mid)" stroke-width="1.3"/>
    <rect x="4" y="60" width="9" height="6" fill="none" stroke="var(--navy-mid)" stroke-width="1"/>
    <path d="M4 60 l4.5 3.5 l4.5 -3.5" fill="none" stroke="var(--navy-mid)" stroke-width="1"/>
  </svg>
</section>

</body>
</html>
```